Boutique Sparkling Blanc de Blancs Wine label

We are looking for a label and neck label for our new Sparkling Chardonnay.
Images uploaded include, bubbles and glitter maybe as a faded background for whole label?
We like Refined, elegant yet simple designs.
Have included our current table chardonnay label as example.

Industry/Entity Type

Boutique

Font styles to use
Decorative
Script

Requirements
Must have
• Name - "Beneath the Lanterns"
• Methode Traditionelle
• Blanc de Blancs
• 2015
• Across the Orchard (Brand)
• Adelaide Hills
Nice to have
• Neutral tones
• Sparkles, Glitter, Bubbles
• Traditional, cursive or vine like fonts
• Have attached fonts we used for previous wine label - might be nice to carry through same/similar fonts to continue our brand?
Should not have
• a lot of colour

```html
<!DOCTYPE html>
<html lang="en">
<head>
<meta charset="utf-8">
<title>Beneath the Lanterns – Sparkling Chardonnay Label</title>
<link rel="stylesheet" href="https://fonts.googleapis.com/css2?family=Kaushan+Script&family=Noto+Serif:ital@0;1&display=swap">
<style>
  :root {
    --backdrop: #1a2606;
    --night: #1b1740;
    --night-deep: #0f0c2a;
    --gold: #e1b347;
    --gold-light: #f7dc84;
    --gold-dark: #9c6b17;
    --ink: #222222;
    --ribbon: #fbfaf7;
    --ribbon-shade: #ece8df;
  }
  * { margin: 0; padding: 0; box-sizing: border-box; }
  html, body {
    width: 1081px;
    height: 1200px;
    overflow: hidden;
    background: var(--backdrop);
  }
  .label {
    position: absolute;
    left: 190px;
    top: 200px;
    width: 700px;
    height: 800px;
    overflow: hidden;
    box-shadow: 0 4px 18px rgba(0,0,0,0.45);
  }
  .label__artwork {
    position: absolute;
    inset: 0;
    background:
      radial-gradient(ellipse 260px 240px at 340px 330px, rgba(225,179,71,0.28), transparent 70%),
      radial-gradient(ellipse 420px 120px at 560px 60px, rgba(225,170,80,0.45), transparent 70%),
      linear-gradient(to bottom, var(--night-deep) 0%, var(--night) 45%, #3a2f3a 58%, #a27a2c 64%, var(--gold) 74%, #c9952f 100%);
  }
  .label__ribbon {
    position: absolute;
    inset: 0;
    width: 700px;
    height: 800px;
  }
  .label__title {
    position: absolute;
    font-family: "Kaushan Script", cursive;
    color: var(--gold);
    background: linear-gradient(180deg, var(--gold-light) 0%, var(--gold) 50%, var(--gold-dark) 100%);
    -webkit-background-clip: text;
    background-clip: text;
    -webkit-text-fill-color: transparent;
    filter: drop-shadow(4px 5px 0 #1c1a12);
    white-space: nowrap;
    line-height: 1;
    transform-origin: center;
  }
  .label__title--top {
    left: 290px;
    top: 275px;
    font-size: 76px;
    transform: translate(-50%, -50%) rotate(-22deg);
  }
  .label__title--bottom {
    left: 420px;
    top: 410px;
    font-size: 92px;
    transform: translate(-50%, -50%) rotate(-18deg);
  }
  .label__variety {
    position: absolute;
    left: 337px;
    top: 655px;
    transform: translate(-50%, -50%) rotate(-11deg);
    font-family: "Noto Serif", serif;
    font-style: italic;
    font-size: 40px;
    color: var(--ink);
    white-space: nowrap;
    letter-spacing: 0.5px;
  }
  .label__vintage {
    position: absolute;
    left: 352px;
    top: 771px;
    transform: translate(-50%, -50%);
    font-family: "Noto Serif", serif;
    font-size: 29px;
    color: var(--ink);
  }
</style>
</head>
<body>
  <main class="label">
    <div class="label__artwork" role="img" aria-label="Swirling ring of gold glitter and warm bokeh lights over a deep indigo night, settling into a bed of gold glitter"></div>

    <svg class="label__ribbon" viewBox="0 0 700 800" aria-hidden="true">
      <defs>
        <linearGradient id="ribbon-fill" x1="0" y1="0" x2="0" y2="1">
          <stop offset="0" stop-color="var(--ribbon-shade)"/>
          <stop offset="0.5" stop-color="var(--ribbon)"/>
          <stop offset="1" stop-color="var(--ribbon-shade)"/>
        </linearGradient>
        <linearGradient id="ribbon-edge" x1="0" y1="0" x2="1" y2="0">
          <stop offset="0" stop-color="#8a5e1a"/>
          <stop offset="0.5" stop-color="#f2d27a"/>
          <stop offset="1" stop-color="#8a5e1a"/>
        </linearGradient>
      </defs>
      <path d="M0,478 C150,560 300,615 440,570 C560,530 640,520 700,560 L700,780 C610,700 500,690 400,725 C260,770 120,760 0,700 Z"
            fill="url(#ribbon-fill)"/>
      <path d="M0,478 C150,560 300,615 440,570 C560,530 640,520 700,560"
            fill="none" stroke="url(#ribbon-edge)" stroke-width="5"/>
      <path d="M700,780 C610,700 500,690 400,725 C260,770 120,760 0,700"
            fill="none" stroke="url(#ribbon-edge)" stroke-width="5"/>
    </svg>

    <h1>
      <span class="label__title label__title--top">Beneath the</span>
      <span class="label__title label__title--bottom">Lanterns</span>
    </h1>
    <p class="label__variety">Sparkling Chardonnay</p>
    <p class="label__vintage">2015</p>
  </main>
</body>
</html>
```